Pebble

My company name is pebble. The logo is attached. I am the business owner.
Name Gideon Thorpe
Phone number- 5553018826
email- Gideon_thorpe@quillnet.net
Website is not live yet but it will be workwithpebble.com
the current beta link is- https://site.brvhosting.com/pebble-v3/
on the back write “ find creative pros”
Use that beta link as reference for typography and colors on card.

```html
<!DOCTYPE html>
<html lang="en">
<head>
<meta charset="UTF-8">
<title>Pebble — Business Card</title>
<link rel="stylesheet" href="https://fonts.googleapis.com/css2?family=Montserrat:wght@400;500;600;800&display=swap">
<style>
  :root {
    --backdrop: #cfd3d4;
    --paper: #f2f1ef;
    --ink-black: #1c1b1b;
    --brand-red: #a8220f;
    --text-dark: #262626;
    --rule: #3a3a3a;
    --tagline: #ecebea;
  }
  * { margin: 0; padding: 0; box-sizing: border-box; }
  html, body {
    width: 1200px;
    height: 1050px;
    overflow: hidden;
    background: var(--backdrop);
    font-family: "Montserrat", Arial, sans-serif;
  }
  .canvas {
    width: 1200px;
    height: 1050px;
    display: flex;
    flex-direction: column;
    align-items: center;
    justify-content: center;
    gap: 60px;
  }
  .card {
    position: relative;
    width: 740px;
    height: 423px;
    border-radius: 4px;
    box-shadow: 0 18px 40px rgba(0,0,0,0.18);
  }

  /* Front side */
  .card--front { background: var(--paper); color: var(--text-dark); }
  .wordmark {
    font-family: "Montserrat", Arial, sans-serif;
    font-weight: 800;
    color: var(--brand-red);
    letter-spacing: 0.01em;
    line-height: 1;
  }
  .card--front .wordmark {
    position: absolute;
    top: 56px;
    right: 52px;
    font-size: 86px;
  }
  .holder {
    position: absolute;
    top: 112px;
    left: 52px;
  }
  .holder__name {
    font-size: 26px;
    font-weight: 600;
    color: var(--brand-red);
    letter-spacing: 0.01em;
    text-transform: uppercase;
  }
  .holder__role {
    margin-top: 4px;
    font-size: 19px;
    font-weight: 600;
    color: var(--text-dark);
  }
  .divider {
    position: absolute;
    left: 130px;
    right: 52px;
    top: 170px;
    height: 1px;
    background: var(--rule);
  }
  .contact-list {
    position: absolute;
    top: 196px;
    left: 52px;
    list-style: none;
  }
  .contact-list__item {
    display: flex;
    align-items: center;
    gap: 10px;
    font-size: 20px;
    font-weight: 500;
    line-height: 1;
    margin-bottom: 14px;
  }
  .contact-list__icon { width: 18px; height: 18px; flex: none; }
  .social {
    position: absolute;
    right: 110px;
    bottom: 44px;
    display: flex;
    flex-direction: column;
    align-items: center;
    gap: 10px;
  }
  .social__dots { display: flex; gap: 8px; }
  .social__dot {
    width: 20px;
    height: 20px;
    border-radius: 50%;
    background: var(--brand-red);
  }
  .social__handle { font-size: 20px; font-weight: 500; }

  /* Back side */
  .card--back {
    background: var(--ink-black);
    display: flex;
    flex-direction: column;
    align-items: center;
    justify-content: center;
  }
  .card--back .wordmark { font-size: 116px; }
  .tagline {
    margin-top: 26px;
    font-size: 19px;
    font-weight: 500;
    letter-spacing: 0.22em;
    color: var(--tagline);
    text-transform: uppercase;
  }
</style>
</head>
<body>
<main class="canvas">

  <section class="card card--front" aria-label="Business card front">
    <div class="wordmark">PEBBLE</div>

    <div class="holder">
      <p class="holder__name">Gideon Thorpe</p>
      <p class="holder__role">Owner</p>
    </div>
    <div class="divider"></div>

    <ul class="contact-list">
      <li class="contact-list__item">
        <svg class="contact-list__icon" viewBox="0 0 24 24" aria-hidden="true">
          <path fill="var(--brand-red)" d="M6.6 10.8a15.1 15.1 0 0 0 6.6 6.6l2.2-2.2a1 1 0 0 1 1-.25 11.4 11.4 0 0 0 3.6.57 1 1 0 0 1 1 1V20a1 1 0 0 1-1 1A17 17 0 0 1 3 4a1 1 0 0 1 1-1h3.5a1 1 0 0 1 1 1c0 1.25.2 2.45.57 3.57a1 1 0 0 1-.25 1z"/>
        </svg>
        <span>5553018826</span>
      </li>
      <li class="contact-list__item">
        <svg class="contact-list__icon" viewBox="0 0 24 24" aria-hidden="true">
          <rect x="2" y="5" width="20" height="14" rx="1" fill="var(--brand-red)"/>
          <path d="M3 6l9 7 9-7" fill="none" stroke="var(--paper)" stroke-width="1.6"/>
        </svg>
        <span>Gideon_thorpe@quillnet.net</span>
      </li>
      <li class="contact-list__item">
        <svg class="contact-list__icon" viewBox="0 0 24 24" aria-hidden="true">
          <g fill="none" stroke="var(--brand-red)" stroke-width="1.8">
            <circle cx="12" cy="12" r="9.5"/>
            <ellipse cx="12" cy="12" rx="4.2" ry="9.5"/>
            <path d="M2.5 12h19M4 7h16M4 17h16"/>
          </g>
        </svg>
        <span>www.workwithpebble.com</span>
      </li>
    </ul>

    <div class="social">
      <div class="social__dots" aria-hidden="true">
        <span class="social__dot"></span>
        <span class="social__dot"></span>
        <span class="social__dot"></span>
      </div>
      <span class="social__handle">@workwithpebble</span>
    </div>
  </section>

  <section class="card card--back" aria-label="Business card back">
    <div class="wordmark">PEBBLE</div>
    <p class="tagline">Find creative pros</p>
  </section>

</main>
</body>
</html>
```